Art Exhibit Invitation Design

This is an exhibit invitation for a three-artist show. The final postcard will be 6X9 and placed in an envelope of 6 1/2 by 9 1/2. I have placed two logos we use (although the logo color is pink, it is possible that the color can be changed. The artists are Marla Bennick, Lynette Paulsen, and Rosalind Metcalf. The corresponding images are Lynette (apple tree), Rosalind (green celadon), and Marla (Poppies). The show runs July 8 - Aug 25. The opening Reception is Saturday, July 8 from 3-5pm. I would like this done in Adobe InDesign. Since the postcard is being put in an envelope, information about the exhibit can be put on the back (no return address or stamp will be needed) .
The Quimby Gallery is located at 2813 E Fernwood Ave, Yakima WA 98907. our phone is (509) 555-0193.
The exhibit title is Quiet Harvest.
Lynette works in Pastel, Marla is a painter, and Rosalnd is a ceramicist.

```html
<!DOCTYPE html>
<html lang="en">
<head>
<meta charset="utf-8">
<title>Quiet Harvest – Art Exhibit Invitation</title>
<link href="https://fonts.googleapis.com/css2?family=Poppins:wght@400;500;600;700&family=Kaushan+Script&display=swap" rel="stylesheet">
<style>
  :root{
    --stage:#2d2d2d;
    --ink:#0d0d0d;
    --paper:#fff8f1;
    --peach:#fbd3ad;
    --orange:#f7942a;
    --orange-deep:#f58220;
    --white:#ffffff;
    --tree-sky:#d9b0a8;
    --tree-green:#5f8a4a;
    --celadon:#a9dccd;
    --cloth:#1d2438;
    --poppy:#d9532a;
    --poppy-wall:#e9df8a;
  }
  *{margin:0;padding:0;box-sizing:border-box}
  html,body{width:1200px;height:1200px;overflow:hidden;background:var(--stage)}
  body{position:relative;font-family:'Poppins',sans-serif;color:var(--ink)}

  .card{
    position:absolute;left:204px;width:792px;height:535px;overflow:hidden;
    box-shadow:0 6px 18px rgba(0,0,0,.45);
  }
  .card--front{
    top:50px;
    background:
      radial-gradient(ellipse 260px 170px at 88% 18%, rgba(247,130,32,.85), transparent 70%),
      radial-gradient(ellipse 220px 150px at 70% 2%, rgba(247,130,32,.7), transparent 70%),
      radial-gradient(ellipse 240px 140px at 10% 10%, rgba(247,148,42,.55), transparent 70%),
      radial-gradient(ellipse 200px 180px at 95% 75%, rgba(247,148,42,.6), transparent 70%),
      radial-gradient(ellipse 260px 160px at 5% 80%, rgba(247,148,42,.55), transparent 70%),
      radial-gradient(ellipse 380px 260px at 50% 55%, #fff4ea, transparent 80%),
      var(--peach);
  }
  .card--back{
    top:620px;
    background:
      radial-gradient(ellipse 420px 170px at 45% 10%, rgba(247,148,42,.8), transparent 75%),
      radial-gradient(ellipse 300px 160px at 10% 40%, rgba(247,148,42,.65), transparent 75%),
      radial-gradient(ellipse 300px 140px at 80% 30%, rgba(247,130,32,.55), transparent 75%),
      radial-gradient(ellipse 260px 140px at 15% 75%, rgba(250,170,90,.5), transparent 75%),
      linear-gradient(180deg, var(--peach) 0%, #fde3c8 55%, var(--paper) 85%);
  }

  .wordmark{
    position:absolute;font-weight:600;letter-spacing:.16em;color:var(--ink);
    text-transform:uppercase;line-height:1;
  }
  .card--front .wordmark{top:20px;left:0;width:100%;text-align:center;font-size:42px;padding-left:.16em}
  .card--back .wordmark{left:578px;top:466px;font-size:40px}

  .centered{position:absolute;left:0;width:100%;text-align:center;line-height:1}
  .invite-lead{top:91px;font-size:21px;font-weight:400}
  .exhibit-title{top:112px;font-family:'Kaushan Script',cursive;font-size:82px;font-weight:400}
  .exhibit-kind{top:216px;font-size:36px;font-weight:400;letter-spacing:.4em;padding-left:.4em}

  .artwork{
    position:absolute;top:266px;width:207px;height:207px;border:4px solid var(--white);
  }
  .artwork--orchard{left:42px;background:linear-gradient(170deg,var(--tree-sky) 0%,#8a9a62 40%,var(--tree-green) 70%,#6f9c58 100%)}
  .artwork--celadon{left:294px;background:radial-gradient(circle at 50% 50%,var(--celadon) 0 48%,var(--cloth) 50%)}
  .artwork--poppies{left:546px;background:linear-gradient(180deg,var(--poppy-wall) 0%,#e5b561 40%,var(--poppy) 60%,#3f8a86 100%)}

  .brush-label{position:absolute;top:481px;width:180px;height:28px}
  .brush-label svg{position:absolute;inset:0;width:100%;height:100%}
  .brush-label span{position:relative;display:block;text-align:center;line-height:28px;color:var(--white);font-size:16.5px}
  .brush-label--1{left:56px}
  .brush-label--2{left:311px}
  .brush-label--3{left:559px}

  .feature-lead{top:28px;font-size:19px;font-weight:500}
  .artist{position:absolute;top:84px;width:260px;text-align:center;line-height:1}
  .artist__name{display:block;font-size:25px;font-weight:700;color:var(--white)}
  .artist__medium{display:block;margin-top:14px;font-family:'Kaushan Script',cursive;font-size:25px}
  .artist--1{left:4px}
  .artist--2{left:271px}
  .artist--3{left:529px}
  .divider{position:absolute;top:84px;width:10px;height:74px}
  .divider--1{left:255px}
  .divider--2{left:542px}

  .run-dates{position:absolute;left:137px;top:200px;width:525px;height:74px}
  .run-dates svg{position:absolute;inset:0;width:100%;height:100%}
  .run-dates span{position:relative;display:block;text-align:center;line-height:74px;font-size:44px;font-weight:700;color:var(--white);letter-spacing:-.01em}

  .reception-lead{top:300px;font-size:21px;font-weight:400}
  .reception-time{top:343px;font-size:36px;font-weight:700;letter-spacing:-.01em}

  .contact{position:absolute;left:24px;top:460px;font-size:16px;line-height:1}
  .contact li{list-style:none;display:flex;align-items:center;gap:11px;height:28px}
  .contact svg{width:16px;height:16px;flex:none}
</style>
</head>
<body>

<section class="card card--front">
  <div class="wordmark">Quimby</div>
  <p class="centered invite-lead">Invites You To</p>
  <h1 class="centered exhibit-title">Quiet Harvest</h1>
  <p class="centered exhibit-kind">Art Exhibit</p>

  <div class="artwork artwork--orchard" role="img" aria-label="Pastel of an apple orchard with red apples under a pink sky"></div>
  <div class="artwork artwork--celadon" role="img" aria-label="Carved green celadon ceramic platter on dark cloth"></div>
  <div class="artwork artwork--poppies" role="img" aria-label="Painting of red poppies in a white vase"></div>

  <div class="brush-label brush-label--1">
    <svg viewBox="0 0 180 28" preserveAspectRatio="none"><path d="M4 5 L176 3 L170 13 L179 24 L8 26 L2 15 Z" fill="var(--ink)"/></svg>
    <span>Lynette Paulsen</span>
  </div>
  <div class="brush-label brush-label--2">
    <svg viewBox="0 0 180 28" preserveAspectRatio="none"><path d="M4 5 L176 3 L170 13 L179 24 L8 26 L2 15 Z" fill="var(--ink)"/></svg>
    <span>Rosalind Metcalf</span>
  </div>
  <div class="brush-label brush-label--3">
    <svg viewBox="0 0 180 28" preserveAspectRatio="none"><path d="M4 5 L176 3 L170 13 L179 24 L8 26 L2 15 Z" fill="var(--ink)"/></svg>
    <span>Marla Bennick</span>
  </div>
</section>

<section class="card card--back">
  <p class="centered feature-lead">Come and Attend the Three-artist Show Featuring:</p>

  <div class="artist artist--1"><span class="artist__name">Lynette Paulsen</span><span class="artist__medium">Pastel Artist</span></div>
  <svg class="divider divider--1" viewBox="0 0 10 74"><line x1="5" y1="0" x2="5" y2="74" stroke="var(--ink)" stroke-width="1.5"/><circle cx="5" cy="36" r="5" fill="var(--ink)"/></svg>
  <div class="artist artist--2"><span class="artist__name">Rosalind Metcalf</span><span class="artist__medium">Ceramicist</span></div>
  <svg class="divider divider--2" viewBox="0 0 10 74"><line x1="5" y1="0" x2="5" y2="74" stroke="var(--ink)" stroke-width="1.5"/><circle cx="5" cy="36" r="5" fill="var(--ink)"/></svg>
  <div class="artist artist--3"><span class="artist__name">Marla Bennick</span><span class="artist__medium">Painter</span></div>

  <div class="run-dates">
    <svg viewBox="0 0 525 74" preserveAspectRatio="none"><path d="M22 8 L515 4 L505 22 L522 26 L508 44 L516 60 L70 70 L12 64 L24 48 L2 34 L18 22 Z" fill="var(--ink)"/></svg>
    <span>July 8 - Aug 25</span>
  </div>

  <p class="centered reception-lead">The Opening Reception:</p>
  <p class="centered reception-time">Saturday, July 8 from 3-5pm</p>

  <ul class="contact">
    <li>
      <svg viewBox="0 0 16 16"><path d="M8 1a5 5 0 0 0-5 5c0 3.5 5 8 5 8s5-4.5 5-8a5 5 0 0 0-5-5z" fill="none" stroke="var(--orange)" stroke-width="1.6"/><circle cx="8" cy="6" r="1.8" fill="none" stroke="var(--orange)" stroke-width="1.4"/></svg>
      <span>2813 E Fernwood Ave, Yakima WA 98907</span>
    </li>
    <li>
      <svg viewBox="0 0 16 16"><path d="M3 2l3 0 1 4-2 1c1 2 2 3 4 4l1-2 4 1 0 3c-6 1-12-5-11-11z" fill="none" stroke="var(--orange)" stroke-width="1.5" stroke-linejoin="round"/></svg>
      <span>(509) 555-0193</span>
    </li>
  </ul>

  <div class="wordmark">Quimby</div>
</section>

</body>
</html>
```